Personal Business Card

Looking for a clean and modern personal business card. Basically I need something catchy to give to potential clients and people I meet. I do a lot of freelancing (from DJ'ing to wedding videography, but its mostly on the event side of things) so it's more-so about selling myself rather than identifying with a company. I'm starting to meet more people that I want to work with after meeting them so I'm revamping my business cards.

I'm looking for a clean and modern design- I know that's really vague but I'm fine with anything ranging from a symbol to just a fancy version of my name.

Details I need on the front:
Dennis Kowal
dennis@denniskowal-mail.net
(555) 807-2291

On the back I'd like to have something simple like "Nice to have met you today" or "Great meeting you".

UPDATE 9/27 Noon: My apologies for not putting it up before- I'm definitely looking for full color. Doesn't have to be a rainbow but I am looking for the least amount of blank white as possible.

UPDATE 10/1: Really impressed with what I've been getting so far and I'm working on giving everyone feedback- if your design is still up then you're still in the run. Looking for something more unique and modern so please do not post something that looks like a template from Cardloom!

Target Market(s)

Mainly to give to people aged 18-35. Most of my encounters will be casual so the card should have a "young" feeling to it. I rarely do anything in the corporate world so it doesn't have to be boring. It should give the impression that I'm the one they should go to if they need what I do (again it changes every weekend so I'll probably say the "what I do" part.

Industry/Entity Type

Wedding

Requirements
Must have
• Basically the contact information listed above
Nice to have
• I really like the colors Blue, Silver, and Purple. They don't have to necessarily all be there though. I do like the look of polished metal if that makes sense.
Should not have
• A template that resembles card-loom. I'm in a point in my life where I'm working a lot of different markets/areas so the card does not need to have an address or address placeholder.

```html
<!DOCTYPE html>
<html lang="en">
<head>
<meta charset="utf-8">
<title>Great meeting you – card back</title>
<link href="https://fonts.googleapis.com/css2?family=Questrial&display=swap" rel="stylesheet">
<style>
  :root {
    --page: #ffffff;
    --card: #d8d8d8;
    --ink: #393b3b;
    --accent: #e56a4c;
    --tone-teal: #1fb0b6;
    --tone-charcoal: #3a3f3f;
    --tone-orange: #e4644a;
    --tone-rose: #c2445f;
  }
  html, body {
    margin: 0;
    padding: 0;
    width: 1200px;
    height: 1000px;
    overflow: hidden;
    background: var(--page);
  }
  .card-back {
    position: absolute;
    left: 38px;
    top: 163px;
    width: 1125px;
    height: 674px;
    overflow: hidden;
    background: linear-gradient(135deg, #dadada 0%, var(--card) 60%, #d2d2d2 100%);
  }
  .card-back__artwork {
    position: absolute;
    inset: 0;
  }
  .card-back__greeting {
    position: absolute;
    left: 80px;
    top: 330px;
    margin: 0;
    font-family: "Questrial", sans-serif;
    font-weight: 400;
    font-size: 77px;
    letter-spacing: 0.5px;
    line-height: 1;
    color: var(--ink);
    white-space: nowrap;
  }
  .card-back__initial {
    color: var(--accent);
  }
</style>
</head>
<body>
  <section class="card-back">
    <svg class="card-back__artwork" viewBox="0 0 1125 674" width="1125" height="674"
         role="img" aria-label="Abstract decorative artwork in teal, charcoal, orange and rose tones">
      <defs>
        <linearGradient id="artwork-tones" x1="0.2" y1="0" x2="0.9" y2="1">
          <stop offset="0" stop-color="var(--tone-teal)"/>
          <stop offset="0.35" stop-color="var(--tone-charcoal)"/>
          <stop offset="0.7" stop-color="var(--tone-orange)"/>
          <stop offset="1" stop-color="var(--tone-rose)"/>
        </linearGradient>
      </defs>
      <path fill="url(#artwork-tones)"
            d="M492,0 L1125,0 L1125,674 L922,674 Q780,240 492,0 Z"/>
    </svg>
    <h1 class="card-back__greeting"><span class="card-back__initial">G</span>reat meeting you !</h1>
  </section>
</body>
</html>
```